Transfer Falcon - Cloud Based Data Migration Service for IT Professionals

We are looking for a smart clean website design for an informational site about our services and as a main portal into the service itself. We would like the design completed in WORDPRESS so that it will easily connect with the service.

Transfer Falcon is a cloud based migration service providing (to start with) a online migration tool that we migrate Quillnet Relay mailboxes (email) with all the settings, attachments from one system to another.
The service is aimed at IT professionals, IT companies and IT departments so our customers will be very technology based.

The Service -
IT companies currently migrate email; data and databases. using a very time intensive process which is both expensive and means their customer potentially losses access to its IT for a significant period of time. Additionally there are risks with regards to compatibility between systems and loss of data.
Potential benefits include;
• cost savings
• improved customer service, including reduced downtime
• improved resilience of the process
We are therefore developing cloud based migration software/website which will automate the process, mitigating these issues, as well as providing additional benefits such as the ability to sort and migrate only certain areas of data or certain emails, to check the integrity of the data/emails moved and to also repair corrupted data and emails.
The system will effectively duplicate the data and emails onto the new system over the weeks prior to the completion date. This will enable the IT Company to complete a final synchronisation and then immediately switch over to the new system with no interruption to the end users.
There is also an added benefit that the end users can test the system (with their own data and emails) prior to the switch over date to ensure everything is in place and databases work correctly.
The system will be completely cloud based and therefore easy for the IT Companies to access. They will be able to purchase the use of the system using CoinDrop or credit card and will only need to purchase what they need, this will allow even small local IT companies the facilities which previously would have been cost prohibitive to them.

Some of the sites we like for reference are -
Lanterbox, brightkits, the sky shifter.

We already have a logo design see attached and the website will need to work with this design.
Please message me if you have any questions
We do have the logo in other file formats if required.
Many Thanks

Target Market(s)

IT Sector

Industry/Entity Type

It Service

Number of Pages Required

5+ page

Requirements
Must have
• Front Page
• About Us
• Contact Info
• Blog
• Benefits
• More Information
• Must be Mobile Phone Compatible/friendly
• Log in (button) and support button on all pages (possibley top right)

```html
<!DOCTYPE html>
<html lang="en">
<head>
<meta charset="utf-8">
<title>Transfer Falcon – Cloud Based Migration Service</title>
<link rel="stylesheet" href="https://fonts.googleapis.com/css2?family=Montserrat:wght@400;500;700&family=Quicksand:wght@500;600;700&display=swap">
<style>
  :root {
    --brand-blue: #0aa7dd;
    --brand-blue-dark: #0891c2;
    --ink: #111111;
    --text: #2b2b2b;
    --muted: #8a8a8a;
    --nav-bg: #5b5b5b;
    --section-light: #f2f3f3;
    --hero-bg-a: #f3f3f3;
    --hero-bg-b: #dcdcdc;
    --blog-dark: #1f1714;
    --footer-bg: #050505;
    --white: #ffffff;
    --icon-grey: #c4c4c4;
  }
  * { box-sizing: border-box; margin: 0; padding: 0; }
  html, body { width: 687px; height: 1200px; overflow: hidden; }
  body {
    position: relative;
    font-family: "Quicksand", Arial, sans-serif;
    color: var(--text);
    background: var(--white);
  }
  .abs { position: absolute; }

  /* Hero */
  .hero {
    position: absolute; left: 0; top: 0; width: 687px; height: 340px;
    background: linear-gradient(100deg, var(--hero-bg-b) 0%, var(--hero-bg-a) 45%, #e9e9e9 100%);
    overflow: hidden;
  }
  .hero-portrait {
    position: absolute; left: 60px; top: 0; width: 260px; height: 340px;
    background: radial-gradient(ellipse at 50% 30%, #e4e4e4 0%, #d2d2d2 55%, rgba(220,220,220,0) 80%);
  }
  .brand {
    position: absolute; left: 44px; top: 62px;
    display: flex; align-items: center; gap: 8px;
    font-family: "Montserrat", Arial, sans-serif; font-weight: 700;
    font-size: 17px; letter-spacing: 1px; color: var(--ink); text-transform: uppercase;
  }
  .brand-mark { width: 14px; height: 14px; border-radius: 50%; background: var(--brand-blue); }
  .hero-title {
    position: absolute; left: 45px; top: 157px; width: 300px;
    font-family: "Quicksand", Arial, sans-serif; font-weight: 700;
    font-size: 21px; line-height: 19px; color: var(--brand-blue);
  }
  .hero-copy {
    position: absolute; left: 45px; top: 208px; width: 250px;
    font-size: 8.6px; line-height: 17px; font-weight: 600; color: var(--text);
  }
  .slider-arrows { position: absolute; left: 44px; top: 270px; display: flex; gap: 8px; }
  .slider-arrows svg { display: block; }
  .hero-device {
    position: absolute; left: 398px; top: 20px; width: 244px; height: 300px;
    border-radius: 6px;
    background: linear-gradient(160deg, #2a2f36 0%, #6f8aa6 35%, #a9bccd 60%, #d9dde1 80%, #c9c9c9 100%);
  }

  /* Navigation */
  .main-nav {
    position: absolute; left: 0; top: 340px; width: 687px; height: 48px;
    background: var(--nav-bg);
  }
  .nav-item {
    position: absolute; top: 0; height: 48px; line-height: 48px;
    font-family: "Quicksand", Arial, sans-serif; font-weight: 600;
    font-size: 10.5px; color: var(--white); transform: translateX(-50%);
  }
  .nav-item.is-active {
    left: 88px; width: 72px; transform: none; text-align: center;
    background: var(--brand-blue);
  }

  /* Intro band */
  .intro {
    position: absolute; left: 0; top: 388px; width: 687px; height: 149px;
    background: var(--brand-blue);
  }
  .intro p {
    position: absolute; left: 130px; top: 44px; width: 427px;
    text-align: center; color: var(--white);
    font-family: "Montserrat", Arial, sans-serif; font-weight: 500;
    font-size: 7.9px; line-height: 16.6px;
  }

  /* What we do */
  .services {
    position: absolute; left: 0; top: 537px; width: 687px; height: 239px;
    background: var(--section-light);
  }
  .section-title {
    position: absolute; left: 0; width: 687px; text-align: center;
    font-family: "Montserrat", Arial, sans-serif; font-weight: 700;
    font-size: 24px; color: var(--ink); letter-spacing: -0.5px;
  }
  .services .section-title { top: 35px; }
  .services-lead {
    position: absolute; left: 100px; top: 76px; width: 487px; text-align: center;
    font-family: "Montserrat", Arial, sans-serif; font-weight: 500;
    font-size: 7.6px; line-height: 13px; color: var(--text);
  }
  .service {
    position: absolute; top: 124px; width: 150px; transform: translateX(-50%);
    text-align: center;
  }
  .service svg { display: block; margin: 0 auto; }
  .service-label {
    margin-top: 10px;
    font-family: "Montserrat", Arial, sans-serif; font-weight: 500;
    font-size: 7.4px; color: var(--ink); text-transform: uppercase;
  }
  .service.is-highlighted .service-label { color: var(--brand-blue); }

  /* Benefit tiles */
  .benefit {
    position: absolute; top: 776px; width: 229px; height: 78px;
    display: flex; align-items: center; justify-content: center;
    font-family: "Montserrat", Arial, sans-serif; font-weight: 700;
    font-size: 7.6px; color: var(--ink); text-transform: uppercase;
  }
  .benefit-savings { left: 0; background: linear-gradient(90deg, #d9d2cd 0%, #eee6e2 50%, #f4f1ef 100%); }
  .benefit-service { left: 229px; background: linear-gradient(90deg, #3aa9d2 0%, #2f9ecb 50%, #3ca6d0 100%); color: var(--white); text-decoration: underline; }
  .benefit-resilience { left: 458px; width: 229px; background: linear-gradient(90deg, #e9e7e4 0%, #d9d6d2 60%, #c8c3bd 100%); }

  /* Blog */
  .blog-panel {
    position: absolute; left: 0; top: 854px; width: 344px; height: 202px;
    background: linear-gradient(135deg, #2a201c 0%, var(--blog-dark) 60%, #15100e 100%);
    color: var(--white);
  }
  .blog-panel .blog-title {
    position: absolute; left: 110px; top: 32px;
    font-family: "Montserrat", Arial, sans-serif; font-weight: 700; font-size: 24px;
  }
  .blog-excerpt {
    position: absolute; left: 45px; top: 82px; width: 250px;
    font-family: "Montserrat", Arial, sans-serif; font-weight: 500;
    font-size: 7.8px; line-height: 13.3px;
  }
  .blog-stats {
    position: absolute; left: 45px; top: 128px; display: flex; gap: 14px; align-items: center;
    font-family: "Montserrat", Arial, sans-serif; font-size: 7.8px;
  }
  .blog-stats span { display: flex; align-items: center; gap: 6px; }
  .read-more {
    position: absolute; left: 45px; top: 151px;
    font-family: "Montserrat", Arial, sans-serif; font-weight: 700; font-size: 7.8px;
    color: var(--brand-blue); text-decoration: underline;
  }
  .blog-photo {
    position: absolute; left: 344px; top: 854px; width: 343px; height: 202px;
    background: linear-gradient(135deg, #e9eef2 0%, #b8c2cc 35%, #8f7d72 60%, #4a4f58 100%);
  }

  /* Contact band */
  .contact {
    position: absolute; left: 0; top: 1056px; width: 687px; height: 102px;
    background: var(--brand-blue); color: var(--white);
  }
  .contact-item {
    position: absolute; top: 38px; display: flex; align-items: center; gap: 10px;
    font-family: "Montserrat", Arial, sans-serif; font-weight: 500; font-size: 8.2px; line-height: 12px;
  }
  .contact-icon {
    width: 27px; height: 27px; border-radius: 50%; background: var(--white);
    display: flex; align-items: center; justify-content: center; flex: none;
  }

  /* Footer */
  .site-footer {
    position: absolute; left: 0; top: 1158px; width: 687px; height: 42px;
    background: var(--footer-bg); text-align: center; line-height: 42px;
    font-family: "Quicksand", Arial, sans-serif; font-size: 7px; color: #6b6b6b;
  }
  .site-footer .footer-brand { color: var(--brand-blue); }
</style>
</head>
<body>

<header class="hero">
  <div class="hero-portrait" role="img" aria-label="Faded photo of a smiling businessman in a suit"></div>
  <div class="brand"><span class="brand-mark"></span>Transfer Falcon</div>
  <h1 class="hero-title">Transfer Falcon is a cloud based migration service</h1>
  <p class="hero-copy">Providing (to start with) a online migration tool that we migrate Quillnet Relay mailboxes (email) with all the settings, attachments from one system to another</p>
  <div class="slider-arrows">
    <svg width="18" height="18" viewBox="0 0 18 18"><circle cx="9" cy="9" r="8" fill="none" stroke="#0aa7dd" stroke-width="1.2"/><path d="M10.3 6 L7.3 9 L10.3 12" fill="none" stroke="#0aa7dd" stroke-width="1.2"/></svg>
    <svg width="18" height="18" viewBox="0 0 18 18"><circle cx="9" cy="9" r="8" fill="none" stroke="#ffffff" stroke-width="1.2"/><path d="M7.7 6 L10.7 9 L7.7 12" fill="none" stroke="#ffffff" stroke-width="1.2"/></svg>
  </div>
  <div class="hero-device" role="img" aria-label="Photo of a desktop computer monitor showing a misty mountain landscape"></div>
</header>

<nav class="main-nav">
  <span class="nav-item is-active">Home</span>
  <span class="nav-item" style="left:210px">About Us</span>
  <span class="nav-item" style="left:301px">Services</span>
  <span class="nav-item" style="left:390px">Benefits</span>
  <span class="nav-item" style="left:468px">Blog</span>
  <span class="nav-item" style="left:550px">Contact Us</span>
</nav>

<section class="intro">
  <p>Lorem ipsum dolor sit amet, consectetur adipiscing elit, sed do eiusmod tempor incididunt ut labore et dolore magna aliqua. Ut enim ad minim veniam, quis nostrud exercitation ullamco laboris nisi ut aliquip ex ea commodo consequat. Duis aute irure dolor in reprehenderit in voluptate velit esse cillum dolore eu fugiat nulla pariatur.</p>
</section>

<section class="services">
  <h2 class="section-title">WHAT WE DO</h2>
  <p class="services-lead">We are therefore developing cloud based migration software/website which will automate the process, mitigating these issues, as well as providing additional benefits such as the ability to sort.</p>

  <div class="service" style="left:207px">
    <svg width="58" height="40" viewBox="0 0 58 40"><rect x="1" y="1" width="56" height="38" fill="#d2d2d2" stroke="#bdbdbd"/><path d="M1 1 L29 23 L57 1" fill="none" stroke="#f2f3f3" stroke-width="2"/><path d="M1 39 L22 18 M57 39 L36 18" stroke="#f2f3f3" stroke-width="2"/></svg>
    <div class="service-label">Migrating Mail</div>
  </div>

  <div class="service is-highlighted" style="left:343px">
    <svg width="58" height="52" viewBox="0 0 58 52"><rect x="6" y="12" width="40" height="28" rx="2" fill="none" stroke="#0aa7dd" stroke-width="3"/><rect x="0" y="42" width="56" height="8" rx="2" fill="#0aa7dd"/><circle cx="44" cy="46" r="1.5" fill="#fff"/><circle cx="49" cy="46" r="1.5" fill="#fff"/><path d="M14 18 L14 30 L17 27 L20 33 L22 32 L19 26 L23 26 Z" fill="#0aa7dd"/><path d="M28 36 L44 18" stroke="#0aa7dd" stroke-width="5" stroke-linecap="round"/><rect x="40" y="3" width="12" height="14" rx="2" transform="rotate(40 46 10)" fill="#0aa7dd"/></svg>
    <div class="service-label">Repair Courrupted Date</div>
  </div>

  <div class="service" style="left:474px">
    <svg width="60" height="56" viewBox="0 0 60 56"><path d="M4 4 L36 4 L36 30 C36 42 26 50 20 54 C14 50 4 42 4 30 Z" fill="none" stroke="#c4c4c4" stroke-width="5"/><path d="M14 12 L28 12 L28 30 C28 36 24 41 20 44" fill="none" stroke="#c4c4c4" stroke-width="4"/><circle cx="45" cy="19" r="13" fill="#c4c4c4" stroke="#f2f3f3" stroke-width="2"/><path d="M39 19 L44 24 L52 14" fill="none" stroke="#f2f3f3" stroke-width="3"/></svg>
    <div class="service-label">Secure</div>
  </div>
</section>

<div class="benefit benefit-savings" role="img" aria-label="Photo of a hand dropping a coin into a piggy bank">Cost Savings</div>
<div class="benefit benefit-service" role="img" aria-label="Photo of a smiling team giving thumbs up, tinted blue">Improved Customer Services</div>
<div class="benefit benefit-resilience" role="img" aria-label="Photo of hands typing on a laptop keyboard">Improved Resilience of the Process</div>

<section class="blog-panel">
  <h2 class="blog-title">OUR BLOG</h2>
  <p class="blog-excerpt">Lorem ipsum dolor sit amet, consectetur adipiscing elit, sed do eiusmod tempor incididunt ut labore et dolore magna aliqua.</p>
  <div class="blog-stats">
    <span><svg width="12" height="10" viewBox="0 0 12 10"><path d="M1 1 H8 V6 H4 L2 8 V6 H1 Z" fill="#fff"/><path d="M9 3 H11 V8 H10 V10 L8 8 H5 V7 H9 Z" fill="#fff"/></svg>1000</span>
    <span><svg width="13" height="9" viewBox="0 0 13 9"><path d="M0.5 4.5 C3 0 10 0 12.5 4.5 C10 9 3 9 0.5 4.5 Z" fill="#fff"/><circle cx="6.5" cy="4.5" r="2.2" fill="#1f1714"/></svg>12.2500</span>
  </div>
  <span class="read-more">READ MORE</span>
</section>
<div class="blog-photo" role="img" aria-label="Photo of hands holding a smartphone in front of a laptop"></div>

<section class="contact">
  <div class="contact-item" style="left:133px; top:40px">
    <span class="contact-icon"><svg width="9" height="12" viewBox="0 0 9 12"><path d="M4.5 0 C7 0 9 2 9 4.5 C9 7.5 4.5 12 4.5 12 C4.5 12 0 7.5 0 4.5 C0 2 2 0 4.5 0 Z" fill="#111"/><circle cx="4.5" cy="4.5" r="1.7" fill="#fff"/></svg></span>
    <span>Lorem ipsum dolor sit amet,<br>consectetur adipiscing elit,</span>
  </div>
  <div class="contact-item" style="left:313px; top:40px">
    <span class="contact-icon"><svg width="8" height="12" viewBox="0 0 8 12"><rect x="0.5" y="0.5" width="7" height="11" rx="1.2" fill="#111"/><rect x="1.8" y="2" width="4.4" height="6.5" fill="#fff"/></svg></span>
    <span>+01234567890</span>
  </div>
  <div class="contact-item" style="left:443px; top:40px">
    <span class="contact-icon"><svg width="11" height="8" viewBox="0 0 11 8"><rect width="11" height="8" rx="1" fill="#111"/><path d="M0.5 0.8 L5.5 4.5 L10.5 0.8" fill="none" stroke="#fff" stroke-width="1"/></svg></span>
    <span>xyz@example.com</span>
  </div>
</section>

<footer class="site-footer">© <span class="footer-brand">Transfer Falcon</span> - 2016. All Rights Reserved.</footer>

</body>
</html>
```